New business card/stationary for a consulting company

I am looking for a clean and very professional looking business card for my consulting company as well as corresponding stationary. I am uploading our logo. I like simple and powerful for the feel. No graphics but I am open on everything else. Below is my contact information but would like the final to be in a version I can add my employees information into and print. Thank you.

Daniel Whitcombe
dan@fernlowadvisory.com
2837 North 9th Avenue, Summit Floor, Larkmere, Westland 60483
www.fernlowadvisory.com

Industry/Entity Type

Consulting

Contact Information for Business Card

Daniel Whitcombe
dan@fernlowadvisory.com
www.fernlowadvisory.com

Font styles to use
Serif
Sans Serif

Requirements
Must have
• Our logo and the business card details.
Nice to have
• our website www.fernlowadvisory.com

```html
<!DOCTYPE html>
<html lang="en">
<head>
<meta charset="UTF-8">
<title>Fernlow Advisory — Business Card</title>
<link rel="stylesheet" href="https://fonts.googleapis.com/css2?family=Cinzel:wght@700&family=Questrial&display=swap">
<style>
  :root {
    --page-bg: #e9e9ea;
    --card-bg: #ffffff;
    --band: #000000;
    --ink: #111111;
    --text-grey: #3a3a3a;
    --brand-navy: #2b2466;
    --name-white: #ffffff;
  }
  html, body {
    margin: 0;
    padding: 0;
    width: 1200px;
    height: 1200px;
    overflow: hidden;
    background: var(--page-bg);
  }
  .canvas {
    position: relative;
    width: 1200px;
    height: 1200px;
  }
  .business-card {
    position: absolute;
    left: 75px;
    top: 300px;
    width: 1050px;
    height: 600px;
    background: var(--card-bg);
    box-shadow: 0 2px 10px rgba(0,0,0,0.12);
    overflow: hidden;
  }
  .name-band {
    position: absolute;
    left: 0;
    top: 0;
    width: 100%;
    height: 100px;
    background: var(--band);
  }
  .holder-name {
    position: absolute;
    left: 60px;
    top: 25px;
    margin: 0;
    font-family: "Cinzel", serif;
    font-weight: 700;
    font-size: 40px;
    letter-spacing: 1.5px;
    color: var(--name-white);
    line-height: 1.2;
  }
  .brand {
    position: absolute;
    left: 72px;
    top: 320px;
    display: flex;
    align-items: center;
    gap: 16px;
  }
  .brand-square {
    width: 30px;
    height: 30px;
    background: var(--brand-navy);
  }
  .brand-name {
    font-family: "Questrial", sans-serif;
    font-size: 32px;
    letter-spacing: 0.5px;
    color: var(--brand-navy);
  }
  .timeline {
    position: absolute;
    left: 553px;
    top: 150px;
    width: 6px;
    height: 386px;
    background: var(--ink);
  }
  .contact-item {
    position: absolute;
    left: 537px;
    display: flex;
    align-items: flex-start;
    gap: 20px;
  }
  .contact-item svg {
    flex: none;
    width: 38px;
    height: 38px;
  }
  .contact-text {
    font-family: "Questrial", sans-serif;
    font-size: 21px;
    letter-spacing: 1.4px;
    color: var(--text-grey);
    line-height: 30px;
    padding-top: 4px;
  }
  .contact-email .contact-text,
  .contact-web .contact-text {
    text-transform: uppercase;
  }
  .contact-email { top: 226px; }
  .contact-web { top: 304px; }
  .contact-address { top: 383px; }
  .contact-address .contact-text { font-size: 23px; letter-spacing: 1px; }
</style>
</head>
<body>
<main class="canvas">
  <section class="business-card">
    <header class="name-band">
      <h1 class="holder-name">Daniel Whitcombe</h1>
    </header>

    <div class="brand">
      <span class="brand-square"></span>
      <span class="brand-name">Fernlow Advisory</span>
    </div>

    <div class="timeline"></div>

    <div class="contact-item contact-email">
      <svg viewBox="0 0 36 36" aria-hidden="true">
        <circle cx="18" cy="18" r="18" fill="#000"/>
        <rect x="9" y="12" width="18" height="12" fill="#fff"/>
        <path d="M9 12 L18 19 L27 12" fill="none" stroke="#000" stroke-width="1.6"/>
      </svg>
      <span class="contact-text">dan@fernlowadvisory.com</span>
    </div>

    <div class="contact-item contact-web">
      <svg viewBox="0 0 36 36" aria-hidden="true">
        <circle cx="18" cy="18" r="18" fill="#000"/>
        <g fill="none" stroke="#fff" stroke-width="1.6">
          <circle cx="18" cy="18" r="9"/>
          <ellipse cx="18" cy="18" rx="4" ry="9"/>
          <line x1="9" y1="18" x2="27" y2="18"/>
          <line x1="18" y1="9" x2="18" y2="27"/>
        </g>
      </svg>
      <span class="contact-text">www.fernlowadvisory.com</span>
    </div>

    <div class="contact-item contact-address">
      <svg viewBox="0 0 36 36" aria-hidden="true">
        <circle cx="18" cy="18" r="18" fill="#000"/>
        <path d="M18 8 C13.5 8 11 11.3 11 14.8 C11 19.5 18 28 18 28 C18 28 25 19.5 25 14.8 C25 11.3 22.5 8 18 8 Z" fill="#fff"/>
        <circle cx="18" cy="15" r="2.8" fill="#000"/>
      </svg>
      <span class="contact-text">2837 North 9th Avenue,<br>Summit Floor, Larkmere,<br>Westland 60483</span>
    </div>
  </section>
</main>
</body>
</html>
```